Business card for Industrial Automation Company.

The company is called Process and Motion Solutions. We are a systems integration company in South Africa specializing in PLC and SCADA programming, systems integration and industrial automation. Attached find logo and cover letter of the company for a feel of the general look. The website is still under development, so you will have to use your own ideas.

Please blend the colors on the business card as per the logo colors. Must be clean, professional look. Please submit a creative professional design. If a background color is used please do not use dark colored backgrounds.

Target Market(s)

Mining

Industry/Entity Type

Engineering Consultant

Contact Information for Business Card

Fanie du Plessis (NDip Electrical LC; BSc)
Director / Systems Engineer

Postal Address
PO Box 2836
Duinhoek
7412

Physical Address:
Bloubos Street 27
Duinhoek
7412

Tel: +22 548 6172
Cell: +27 82 395 4820
Mail: faniep@pms-za.example
Web: www.pms-za.example

Font styles to use
Sans Serif

Colors

Designer to choose colors to be used in the design.

Requirements
Must have
• Backside of the card must also contain the following:
• Services
• *Industrial Automation
• *Control System design and configuration
• *Systems Integration
• *Equipment Supply
• Industries
• *Mining
• *Factory
• *Oil and Gas
Nice to have
• Colors must blend in with colors of logo. Not too much color and no dark backgrounds.
Should not have
• dark / black background. Preferably white / light background if any.

```html
<!DOCTYPE html>
<html lang="en">
<head>
<meta charset="utf-8">
<title>Process and Motion Solutions – Business Card</title>
<link rel="stylesheet" href="https://fonts.googleapis.com/css2?family=Lato:wght@400;700;900&display=swap">
<style>
  :root {
    --navy: #1f4587;
    --navy-deep: #183a73;
    --accent: #d9d62a;
    --ink: #4a4d55;
    --rule: #b9bcc3;
    --ghost: #eef0f6;
    --paper: #ffffff;
    --stage: #e8eaee;
  }
  * { box-sizing: border-box; margin: 0; padding: 0; }
  html, body { width: 1200px; height: 800px; overflow: hidden; }
  body {
    background: var(--stage);
    font-family: "Lato", Arial, sans-serif;
    color: var(--ink);
    position: relative;
  }
  .card {
    position: absolute;
    left: 290px;
    width: 620px;
    height: 354px;
    background: var(--paper);
    box-shadow: 0 6px 18px rgba(0,0,0,.15);
    overflow: hidden;
  }
  .card--back { top: 30px; }
  .card--front { top: 416px; }

  /* shared brand block */
  .brand { position: absolute; white-space: nowrap; }
  .brand__name {
    font-weight: 900;
    color: var(--navy);
    font-size: 22px;
    line-height: 1.05;
    letter-spacing: .2px;
  }
  .brand__tagline {
    margin-top: 6px;
    font-size: 12px;
    letter-spacing: 1.4px;
    color: var(--ink);
  }

  /* back side */
  .ghost-mark {
    position: absolute;
    left: -30px; top: 50px;
    width: 260px; height: 260px;
    border-radius: 50%;
    background: var(--ghost);
  }
  .card--back .brand { left: 290px; top: 36px; }
  .offer { position: absolute; left: 330px; }
  .offer--services { top: 100px; }
  .offer--industries { top: 200px; }
  .offer__title {
    font-size: 12px; font-weight: 700; color: var(--navy);
    text-transform: uppercase; letter-spacing: .4px; margin-bottom: 3px;
  }
  .offer__list { list-style: none; }
  .offer__list li {
    font-size: 11.5px; line-height: 17px; padding-left: 14px; position: relative;
  }
  .offer__list li::before {
    content: ""; position: absolute; left: 2px; top: 6px;
    width: 5px; height: 5px; border-radius: 50%; background: var(--accent);
  }
  .back__web {
    position: absolute; right: 40px; bottom: 42px;
    font-size: 13px; font-weight: 700; color: var(--navy);
  }
  .back__rule {
    position: absolute; left: 0; right: 0; bottom: 28px; height: 1px; background: var(--rule);
  }
  .back__band {
    position: absolute; left: 0; right: 0; bottom: 0; height: 24px; background: var(--navy);
  }

  /* front side */
  .front__band {
    position: absolute; left: 0; top: 0; bottom: 0; width: 96px; background: var(--navy);
  }
  .front__rule-v {
    position: absolute; left: 102px; top: 0; bottom: 0; width: 1px; background: var(--rule);
  }
  .front__disc {
    position: absolute; left: 50px; top: 72px; width: 96px; height: 96px;
    border-radius: 50%; background: var(--paper); border: 4px solid var(--navy-deep);
  }
  .card--front .brand { left: 168px; top: 70px; }
  .person { position: absolute; left: 176px; top: 190px; }
  .person__name { font-size: 20px; font-weight: 700; color: var(--navy); }
  .person__quals { font-size: 11px; font-weight: 700; }
  .person__role { font-size: 14px; margin-top: 2px; }
  .person__rule { width: 400px; height: 1px; background: var(--navy); margin: 8px 0 8px; }
  .contact { font-size: 12px; line-height: 18px; white-space: nowrap; }
  .contact b { color: var(--navy); font-weight: 700; }
  .contact .sep { color: var(--navy); padding: 0 5px; }
</style>
</head>
<body>

<section class="card card--back" aria-label="Back of business card">
  <div class="ghost-mark" aria-hidden="true"></div>
  <div class="brand">
    <div class="brand__name">Process and Motion Solutions</div>
    <div class="brand__tagline">Engineering smarter control systems!</div>
  </div>
  <div class="offer offer--services">
    <h3 class="offer__title">Services</h3>
    <ul class="offer__list">
      <li>Industrial Automation</li>
      <li>Control System design and configuration</li>
      <li>Systems Integration</li>
      <li>Equipment Supply</li>
    </ul>
  </div>
  <div class="offer offer--industries">
    <h3 class="offer__title">Industries</h3>
    <ul class="offer__list">
      <li>Mining</li>
      <li>Factory</li>
      <li>Oil and Gas</li>
    </ul>
  </div>
  <div class="back__web">www.pms-za.example</div>
  <div class="back__rule"></div>
  <div class="back__band"></div>
</section>

<section class="card card--front" aria-label="Front of business card">
  <div class="front__band"></div>
  <div class="front__rule-v"></div>
  <div class="front__disc" aria-hidden="true"></div>
  <div class="brand">
    <div class="brand__name">Process and Motion Solutions</div>
    <div class="brand__tagline">Engineering smarter control systems!</div>
  </div>
  <div class="person">
    <div class="person__name">Fanie du Plessis <span class="person__quals">(NDip Electrical LC; BSc)</span></div>
    <div class="person__role">Director / Systems Engineer</div>
    <div class="person__rule"></div>
    <p class="contact"><b>Tel:</b> +22 548 6172<span class="sep">|</span><b>Cell:</b> +27 82 395 4820<span class="sep">|</span><b>Mail:</b> faniep@pms-za.example</p>
    <p class="contact"><b>www.pms-za.example</b></p>
    <p class="contact"><b>Physical Address:</b> Bloubos Street 27, Duinhoek, 7412</p>
    <p class="contact"><b>Postal Address:</b> PO Box 2836, Duinhoek, 7412</p>
  </div>
</section>

</body>
</html>
```